Desktop and Networking Support Course 9.17.25

Important the ad should not be very busy with the text taking up the major part of the ad .. please do not make the text so big that it takes up most of the ad..
Flyer Design Brief for Graphic Artist
also i am looking for something unique or creative that it will stand out .
Size & Layout:
Full Page with Bleed: 8” x 10.75” + 0.25” bleed on all sides.
Footer Space: Leave a 1-inch margin at the bottom for footer content (e.g., contact info, logo, or call-to-action).
Target Audience:
College-age students (around 24 years old)
Located in the USA
Interested in creative, professional, and career-building opportunities
Purpose:
To attract students to enroll in a college program
Flyer should be eye-catching, unique, and creative
Text must be clear and readable,
Design Style:
Use vector art, typography, or photography — your choice
If using photography, feature a white young professional USA citizen:
Wearing a white collared shirt
not with long hair
Creative Direction:
The flyer should stand out visually — something people would want to look at and keep
Showcase creativity and professionalism
Use bold colors, dynamic layout, or unexpected design elements to grab attention
Avoid clutter — keep the design balanced and clean
Text Suggestions (can be adjusted):
Footer,
please leave one inch on the bottom for the footer

```html
<!DOCTYPE html>
<html lang="en">
<head>
<meta charset="UTF-8">
<title>Desktop &amp; Network Support Course Flyer</title>
<link href="https://fonts.googleapis.com/css2?family=Poppins:ital,wght@0,400;0,500;0,600;0,700;1,500&family=Allura&display=swap" rel="stylesheet">
<style>
  :root{
    --navy-deep:#06163f;
    --navy:#0a2260;
    --blue:#1a8fe0;
    --blue-bright:#37b6ff;
    --sky:#4cc4ff;
    --white:#ffffff;
    --panel-line:#2f6fd6;
    --photo-light:#d5dae1;
    --photo-dark:#b8bfc9;
  }
  *{margin:0;padding:0;box-sizing:border-box}
  html,body{width:878px;height:1200px;overflow:hidden}
  body{font-family:"Poppins",sans-serif;color:var(--white);background:var(--navy-deep)}
  .flyer{
    position:relative;width:878px;height:1200px;overflow:hidden;
    background:
      radial-gradient(circle at 85% 12%, rgba(40,170,220,.35), transparent 40%),
      radial-gradient(circle at 20% 35%, rgba(30,90,200,.35), transparent 45%),
      linear-gradient(180deg,var(--navy) 0%,#0a2a72 45%,var(--navy-deep) 100%);
  }
  .script{position:absolute;left:70px;top:66px;font-family:"Allura",cursive;font-size:104px;line-height:1;z-index:2}
  .career{
    position:absolute;left:77px;top:148px;font-weight:700;font-size:78px;line-height:1;letter-spacing:-1px;
    background:linear-gradient(90deg,var(--blue) 0%,var(--sky) 100%);
    -webkit-background-clip:text;background-clip:text;color:transparent;
  }
  .headline-bold{position:absolute;left:77px;font-weight:700;font-size:57px;line-height:1;white-space:nowrap}
  .line-1{top:226px}
  .line-2{top:287px}
  .course{position:absolute;left:77px;top:370px;font-size:35px;line-height:1.15;font-weight:400}
  .photo{
    position:absolute;left:464px;top:190px;width:340px;height:593px;
    border-radius:70px 0 70px 0;
    background:linear-gradient(160deg,var(--photo-light),var(--photo-dark));
  }
  .check{position:absolute;left:79px;width:24px;height:24px}
  .bar{
    position:absolute;left:116px;width:336px;height:61px;border-radius:4px 0 0 4px;
    background:linear-gradient(90deg,var(--blue) 0%,var(--blue) 60%,rgba(26,143,224,0) 100%);
    display:flex;align-items:center;padding-left:18px;
  }
  .bar-1{top:503px;font-size:15px;font-weight:500}
  .bar-2{top:593px;gap:8px}
  .bar-2 .stat{font-size:44px;font-weight:700;line-height:1}
  .bar-2 .label{font-size:16px;font-weight:600;line-height:1.1}
  .bar-2 .label small{display:block;font-size:14px;font-weight:500}
  .bar-3{top:674px;flex-direction:column;align-items:flex-start;justify-content:center}
  .bar-3 .title{font-size:15px;font-weight:600;line-height:1.3}
  .bar-3 .source{font-size:12.5px;font-style:italic;font-weight:500}
  .features{
    position:absolute;left:85px;top:802px;width:713px;height:179px;
    border:1px solid var(--panel-line);border-radius:14px;background:rgba(11,36,96,.85);
    display:flex;padding-top:26px;
  }
  .feature{flex:1;text-align:center;font-size:17px;line-height:1.25}
  .feature svg{display:block;margin:0 auto 14px;width:60px;height:56px}
  .feature + .feature{border-left:1px solid rgba(255,255,255,.7);height:108px}
  .pill{
    position:absolute;top:1034px;width:351px;height:46px;border:1px solid var(--panel-line);
    border-radius:5px;background:#0b2a78;display:flex;align-items:center;gap:10px;
    padding-left:14px;font-size:18px;font-weight:500;
  }
  .pill-left{left:81px}
  .pill-right{left:445px;font-weight:600}
  .pill .dot{width:13px;height:13px;border-radius:50%;background:var(--blue-bright);flex:none}
</style>
</head>
<body>
<div class="flyer">
  <span class="career">Career</span>
  <span class="script">Your</span>
  <span class="headline-bold line-1">IS JUST A</span>
  <span class="headline-bold line-2">CLICK AWAY</span>
  <div class="course">Desktop &amp; Network<br>Support Course</div>

  <div class="photo" role="img" aria-label="Smiling young professional in a white collared shirt, arms crossed"></div>

  <svg class="check" style="top:522px" viewBox="0 0 24 24"><path d="M2 12l7 8L22 3" fill="none" stroke="#37b6ff" stroke-width="3"/></svg>
  <div class="bar bar-1">Master Vantage Operating Systems</div>

  <svg class="check" style="top:612px" viewBox="0 0 24 24"><path d="M2 12l7 8L22 3" fill="none" stroke="#37b6ff" stroke-width="3"/></svg>
  <div class="bar bar-2"><span class="stat">90%</span><span class="label">Employment Rate<small>Class of 2024</small></span></div>

  <svg class="check" style="top:693px" viewBox="0 0 24 24"><path d="M2 12l7 8L22 3" fill="none" stroke="#37b6ff" stroke-width="3"/></svg>
  <div class="bar bar-3"><span class="title">Prepare for 3 of the Top 10 Tech Jobs</span><span class="source">Career Outlook Review 2025</span></div>

  <div class="features">
    <div class="feature">
      <svg viewBox="0 0 60 56" fill="none" stroke="#fff" stroke-width="2"><rect x="3" y="3" width="54" height="38" rx="2"/><path d="M24 41v8M36 41v8M18 51h24"/><rect x="9" y="9" width="12" height="10"/><rect x="15" y="15" width="12" height="10"/><path d="M32 11h18M32 17h18M32 23h18M32 29h10"/></svg>
      Hands-On Desktop<br>&amp; Network Training
    </div>
    <div class="feature">
      <svg viewBox="0 0 60 56" fill="none" stroke="#fff" stroke-width="2"><circle cx="30" cy="30" r="24"/><path d="M16 18l28 26M44 16L18 44M40 8v6M46 8v6M38 14h10"/></svg>
      Real-World<br>Troubleshooting Skills
    </div>
    <div class="feature">
      <svg viewBox="0 0 60 56" fill="none" stroke="#fff" stroke-width="2"><circle cx="30" cy="26" r="18" stroke-dasharray="6 3"/><circle cx="30" cy="21" r="6"/><path d="M20 38c2-7 18-7 20 0"/><path d="M8 44h44M14 50h32"/></svg>
      Ready for<br>IT Jobs
    </div>
  </div>

  <div class="pill pill-left"><span class="dot"></span>In-Person and Remote Options</div>
  <div class="pill pill-right"><span class="dot"></span>Partial Scholarships Offered</div>
</div>
</body>
</html>
```